Webdesign für Sexualpädagogik
Zielgruppe
- Sexualpädagogik, Beratung und Sexualtherapie
- Vorträge und Seminare für Unternehmen / Institutionen Vorträge Sexualität in der Pflege / im Alter / Grenzen wahrnehmen
- Wechseljahreberatung, Beratung in der Lebensmitte
- ZIelgruppe: Menschen, die sich weiternetwickeln möchten, die Problme mit ihrer Sexualität haben, Paare, Jugendliche
letztes Interview in der Zeitung: https://www.talbote-beispiel.ch/talbote/zeitung/frontal-interview/sexualitaet-hoert-nicht-beim-eintritt-ins-spital-auf/
Aufgabenstellung
- bestehende Internetseite siehe unten: Schrift ist Especial Key von Wolkenweg
- auf dem Briefpapier bisher noch der Fachbuchhandel und Onlinhandel, aber beides nicht mehr
- Bilder zum Thema bereist vorhanden
- für Werbeflyer habe ich die Therapie in dunkelblau gehalten udn in der sexualpädagogik in hellblau
der kramhaus wird aus der website entfernet

```html
<!DOCTYPE html>
<html lang="de">
<head>
<meta charset="utf-8">
<title>Wolkenweg – Beratung</title>
<link href="https://fonts.googleapis.com/css2?family=Roboto:ital,wght@0,300;0,400;0,500;0,700;1,400;1,500&family=Montserrat:wght@500&display=swap" rel="stylesheet">
<style>
  :root{
    --brand:#0a4fad;
    --brand-dark:#1a2f9c;
    --text:#2a2a2a;
    --muted:#6d6d6d;
    --panel:#f4f4f4;
    --line:#dcdcdc;
    --white:#ffffff;
    --hero-a:#e9eef7;
    --hero-b:#b9cdea;
  }
  *{box-sizing:border-box;margin:0;padding:0}
  html,body{width:931px;height:1200px;overflow:hidden;background:var(--white)}
  body{position:relative;font-family:"Roboto",sans-serif;color:var(--text)}

  .side-band{position:absolute;left:0;top:0;width:52px;height:1200px;background:var(--brand)}
  .side-band__name{position:absolute;left:26px;top:212px;transform:translate(-50%,-50%) rotate(-90deg);
    color:var(--white);font-family:"Roboto",sans-serif;font-weight:300;font-size:22px;letter-spacing:3px;white-space:nowrap}

  .brand{position:absolute;left:0;top:0;width:931px;text-align:center}
  .brand__name{position:absolute;left:300px;top:14px;width:520px;display:flex;align-items:center;justify-content:center;gap:10px;
    color:var(--brand-dark);font-weight:500;font-size:34px;letter-spacing:4px;text-transform:uppercase}
  .brand__dot{width:12px;height:12px;border-radius:50%;background:var(--brand-dark)}
  .brand__tagline{position:absolute;left:330px;top:60px;width:400px;font-size:10.5px;font-style:italic;font-weight:500;color:#111}
  .brand__tagline em{color:var(--brand-dark)}
  .brand__owner{position:absolute;left:330px;top:77px;width:400px;font-size:10.5px;font-style:italic;font-weight:500;color:#111}

  .main-nav{position:absolute;left:122px;top:115px;width:693px;height:35px;background:var(--brand)}
  .main-nav a{position:absolute;top:0;line-height:35px;transform:translateX(-50%);color:var(--white);
    text-decoration:none;font-weight:700;font-size:10.5px;white-space:nowrap}

  .hero{position:absolute;left:122px;top:150px;width:693px;height:163px;
    background:linear-gradient(90deg,var(--hero-a) 0%,#dfe6f2 45%,#c9d8ee 70%,var(--hero-b) 100%)}
  .hero__label{position:absolute;left:122px;top:204px;width:184px;height:45px}
  .hero__label svg{position:absolute;inset:0}
  .hero__label span{position:absolute;left:26px;top:0;line-height:45px;color:var(--white);font-weight:300;font-size:23px}

  .inset-photo{position:absolute;left:534px;top:289px;width:256px;height:236px;background:var(--white);border:1px solid #cfcfcf}
  .inset-photo__fill{position:absolute;left:11px;top:11px;width:233px;height:213px;
    background:linear-gradient(160deg,#e8e6e4 0%,#d9b7a0 45%,#c59a80 60%,#34405c 80%,#eeeeee 100%)}

  .copy{position:absolute;left:122px;font-size:9.9px;line-height:19.8px;font-weight:300;color:#1e1e1e}
  .copy p{margin:0}
  .copy--narrow{top:336px;width:381px;text-align:justify}
  .copy--narrow p + p{margin-top:19.8px}
  .copy--wide{top:588px;width:693px}
  .copy--wide .gap{height:19.8px}
  .statement{position:absolute;left:120px;top:807px;font-size:11.6px;font-weight:500;color:var(--brand)}

  .testimonial{position:absolute;left:118px;top:915px;width:696px;height:192px;background:var(--panel);border:1px solid var(--line)}
  .testimonial__arrow{position:absolute;top:92px;width:10px;height:14px}
  .testimonial__avatar{position:absolute;left:64px;top:40px;width:116px;height:116px;border-radius:50%;
    background:radial-gradient(circle at 50% 45%,#e6c7ad 0%,#b98c64 55%,#e9e3dc 100%)}
  .testimonial__quote{position:absolute;left:170px;top:52px;width:32px;height:28px}
  .testimonial__stars{position:absolute;left:228px;top:36px;width:66px;height:12px}
  .testimonial__name{position:absolute;left:228px;top:58px;font-family:"Montserrat",sans-serif;font-weight:500;
    font-size:10.5px;letter-spacing:1.8px;color:#7a7a7a;text-transform:uppercase}
  .testimonial__text{position:absolute;left:228px;top:77px;width:425px;font-size:9.3px;line-height:13.7px;color:var(--muted)}
  .testimonial__rule{position:absolute;left:228px;top:147px;width:17px;height:2px;background:var(--brand)}

  .site-footer{position:absolute;left:116px;top:1106px;width:699px;height:42px;background:var(--brand)}
  .site-footer a{position:absolute;top:0;line-height:42px;color:var(--white);text-decoration:none;font-size:9.3px;white-space:nowrap}
  .site-footer .legal{right:15px;font-weight:500}

  .social{position:absolute;top:1164px;font-size:8px;font-weight:500;color:var(--brand);display:flex;align-items:center;gap:3px}
  .social i{display:inline-block;width:8px;height:8px;border-radius:50%;background:var(--brand)}
</style>
</head>
<body>

<aside class="side-band"><span class="side-band__name">WOLKENWEG</span></aside>

<header class="brand">
  <div class="brand__name"><span class="brand__dot"></span>Wolkenweg</div>
  <p class="brand__tagline">Fachstelle Fur <em>Sexualpadagogik, Beratung</em> und <em>Therapie</em></p>
  <p class="brand__owner">Marta Lindqvist</p>
</header>

<nav class="main-nav">
  <a href="#" style="left:68px">HOME</a>
  <a href="#" style="left:168px">ÜBER MICH</a>
  <a href="#" style="left:284px">GÄSTEBUCH</a>
  <a href="#" style="left:405px">NEWSLETTER</a>
  <a href="#" style="left:512px">PREISE</a>
  <a href="#" style="left:610px">KONTAKT</a>
</nav>

<div class="hero" role="img" aria-label="Foto: lachende Frau mit hellem Pullover vor hellem Hintergrund"></div>
<div class="hero__label">
  <svg width="184" height="45" viewBox="0 0 184 45"><polygon points="0,0 178,0 184,45 0,45" fill="#0a4fad"/></svg>
  <span>Beratung</span>
</div>

<figure class="inset-photo">
  <div class="inset-photo__fill" role="img" aria-label="Foto: Hände bei einer Rückenmassage auf weißem Tuch"></div>
</figure>

<div class="copy copy--narrow">
  <p>Manchmal gibt es Fragen, die einen im Zusammenhang mit dem Problem des Partners/der Partnerin beschäftigen, manchmal hat man selbst ein Problem oder Fragen, die sich um einen selbst drehen. Manchmal wird auch eine Eigenschaft/Verhaltensweise des Partners oder der Partnerin, die für diese/n überhaupt kein Problem ist, für einen selbst zum Problem.</p>
  <p>Von vielen Menschen werden Intimität, Liebe, Geborgenheit und Sexualität als die wichtigsten Grundlagen von Partnerschaft und Ehe gesehen. Sexuelle Probleme können Betroffene und Partner belasten. Unsicherheiten, Ängste vor dem Verlassenwerden und der Einsamkeit und ein Leidensdruck, der über das Ausbleiben der Befriedigung hinausgeht, Verletztsein in Weiblichkeit und Männlichkeit, Verunsicherung des Selbstwertgefühls, sind dann Folgen und Begleiterscheinungen dessen.</p>
</div>

<div class="copy copy--wide">
  <p>Es ist nicht alles so kompliziert und schwer, wie es manchmal Anfangs aussieht. Warum also nicht einen Versuch wagen.</p>
  <div class="gap"></div>
  <p>Vereinbaren Sie mit mir einen Termin.</p>
  <div class="gap"></div>
  <p>Die Beratungen führe ich bei Ihnen oder in der Fachstelle durch.</p>
  <div class="gap"></div>
  <p>Die Länge und damit die Kosten der Beratung hängen natürlich von Ihrem Problem, aber auch ihrem Ziel, das Sie mit der Beratung erreichen wollen, ab. Üblicherweise werde ich Ihnen im Zuge der 1. Antwort einen Vorschlag für die weitere Vorgehensweise machen.</p>
  <p>Die Beratungen finden in der Regel alle 2 - 3 Wochen statt und dauern im Schnitt 90 Minuten. Die Häufigkeit und Dauer hängt von Ihren Fragen und Problemen ab. Im Durchschnitt werden aber meist nicht mehr als 10 - 12 Sitzungen benötigt.</p>
</div>

<p class="statement">Die Fachstelle für Sexualpädagogik und Beratung ist unabhängig von Religion und politischer Zugehörigkeit!</p>

<section class="testimonial">
  <svg class="testimonial__arrow" style="left:23px" viewBox="0 0 10 14"><polyline points="7,2 2,7 7,12" fill="none" stroke="#111" stroke-width="1.6"/></svg>
  <div class="testimonial__avatar" role="img" aria-label="Foto: Porträt einer Frau mit langen Haaren"></div>
  <svg class="testimonial__quote" viewBox="0 0 32 28">
    <path d="M2 14 Q2 3 13 1 L13 6 Q8 7 7.5 12 L14 12 L14 27 L2 27 Z" fill="#0a4fad"/>
    <path d="M18 14 Q18 3 29 1 L29 6 Q24 7 23.5 12 L30 12 L30 27 L18 27 Z" fill="#0a4fad"/>
  </svg>
  <svg class="testimonial__stars" viewBox="0 0 66 12" fill="#0a4fad">
    <polygon id="star" points="5,0 6.3,3.8 10,3.8 7,6.2 8.1,10 5,7.7 1.9,10 3,6.2 0,3.8 3.7,3.8"/>
    <use href="#star" x="14"/><use href="#star" x="28"/><use href="#star" x="42"/><use href="#star" x="56"/>
  </svg>
  <p class="testimonial__name">Jonas Ellerbeck</p>
  <p class="testimonial__text">Lorem ipsum dolor sit amet, consectetuer adipiscing elit. Class aptent taciti sociosqu ad litora torquent per conubia nostra, per inceptos hymenaeos. Nulla non arcu lacinia neque faucibus fringilla. Ut enim ad minim veniam, quis nostrud exercitation ullamco laboris nisi ut aliquip ex ea commodo consequat. Nam quis nulla. Ut tempus purus at lorem.</p>
  <div class="testimonial__rule"></div>
  <svg class="testimonial__arrow" style="left:664px" viewBox="0 0 10 14"><polyline points="3,2 8,7 3,12" fill="none" stroke="#111" stroke-width="1.6"/></svg>
</section>

<footer class="site-footer">
  <a href="#" style="left:15px">Impressum</a>
  <a href="#" style="left:81px">Lageplan</a>
  <a href="#" style="left:138px">News</a>
  <a href="#" style="left:180px">Nächste Seminare</a>
  <a href="#" style="left:275px">Kontakt</a>
  <a href="#" style="left:326px">über Marta Lindqvist / Wolkenweg</a>
  <a href="#" class="legal">Datenschutz | Terms &amp; Bedingungen</a>
</footer>

<a class="social" style="left:742px"><i></i>Netzwerk</a>
<a class="social" style="left:788px"><i></i>Sozial</a>

</body>
</html>
```